Velmo (Pathways for company scale) website

My plan is to offer a marketplace where by businesses (SME and Corporates) are able to post specific requirements, be that debt funding advice or other types of advice (legal/accountant) on the velmo website and advisors can seek to 'pitch' to the client.

clients should be anonymous - maybe a specific client number? (this is reduces the risk of bypass) and have the ability to choose the advisor via the advisors profile.

Advisors could potential use there Netlyne profile to auto complete on Velmo - not sure if this is possible or costs involved, however this would be ideal.

I would think Wordpress would be the best platform for this type of platform, however I would be guided by the experts.

I would need any code written in html 5 to allow for various devices (mobile, tablets, desktop)

Logo design is currently being completed also via Sketch Hive and I'm finalising colours ext now, so could provide advice in due course.

additional requirements (medium to longer term)
longer term I would be looking to add addition aspects to the site including algorithms, specific financial calculations, some of which I would be able to complete myself.

similar websites would be:
https://www.taskquill.example.au
http://www.fundoraxi.example.au

Industry/Entity Type

Debt

Coding

Coded - Design and coding required

```html
<!DOCTYPE html>
<html lang="en">
<head>
<meta charset="utf-8">
<title>Velmo — Pathways for company scale</title>
<link href="https://fonts.googleapis.com/css2?family=Arimo:wght@400;700&display=swap" rel="stylesheet">
<style>
:root{
  --green:#1eb872;
  --green-dark:#179a5e;
  --mint:#c8f1dd;
  --ink:#1b1b1b;
  --text:#333;
  --muted:#555;
  --footer:#121212;
  --white:#fff;
}
*{box-sizing:border-box;margin:0;padding:0}
html,body{width:1200px;height:2429px;overflow:hidden}
body{font-family:"Arimo",Arial,sans-serif;color:var(--text);background:var(--white);position:relative}
.abs{position:absolute}

/* header */
.site-header{position:absolute;left:0;top:0;width:1200px;height:68px;background:var(--white)}
.brand{position:absolute;left:176px;top:10px;font-size:36px;font-weight:700;color:var(--ink);letter-spacing:0.5px;border-bottom:3px solid var(--green);line-height:40px}
.main-nav{position:absolute;left:396px;top:26px;display:flex;font-size:15.5px;color:var(--ink)}
.main-nav span{padding:0 9px;border-left:1px solid #444;line-height:14px}
.main-nav span:first-child{border-left:none;padding-left:0;color:var(--green);padding-right:16px}
.caret{display:inline-block;border:4px solid transparent;border-top-color:#333;margin-left:4px;vertical-align:1px}

/* hero */
.hero{position:absolute;left:0;top:68px;width:1200px;height:640px;background:linear-gradient(110deg,#3a3631 0%,#8a8279 35%,#cfc7bd 55%,#6d655d 80%,#2e2a26 100%);border-bottom:5px solid var(--green)}
.hero-panel{position:absolute;left:664px;top:136px;width:350px;height:366px;background:rgba(30,184,114,.82);border-radius:6px;padding:18px 18px 0 18px;color:var(--white)}
.hero-panel h1{font-size:29px;color:var(--ink);text-align:center;font-weight:700;margin-bottom:20px}
.hero-panel p{font-size:14.6px;line-height:18.4px}
.btn-outline{display:inline-block;border:1.5px solid var(--white);border-radius:4px;font-size:12.5px;padding:2px 14px;margin-top:26px;color:var(--white)}
.hero-actions{position:absolute;left:664px;top:526px;display:flex;gap:8px}
.hero-actions span{background:#2b2b2b;color:var(--white);font-size:13px;height:41px;line-height:41px;padding:0 13px;border-radius:3px}
.hero-actions span:last-child{width:171px;text-align:center}
.dots{position:absolute;left:568px;top:609px;display:flex;gap:10px}
.dots i{width:14px;height:14px;border-radius:50%;border:2px solid var(--white);background:transparent;display:block}
.dots i:first-child{background:var(--green);border-color:var(--green)}

/* services */
.service{position:absolute;top:748px;width:200px}
.service svg{display:block;margin-left:22px}
.service h2{font-size:20px;color:var(--ink);font-weight:700;margin-top:26px;white-space:nowrap}
.service p{font-size:14.6px;line-height:18.5px;margin-top:8px;color:var(--ink)}
.btn-more{position:absolute;top:283px;left:60px;border:1.5px solid var(--green);color:var(--green);border-radius:4px;font-size:12.5px;padding:1px 12px}

.feature{position:absolute;top:1091px;width:250px;text-align:center}
.feature h3{font-size:14.5px;font-weight:700;color:var(--ink);margin-bottom:4px}
.feature .ph{width:250px;height:121px}
.feature p{font-size:14.2px;line-height:17.5px;margin-top:8px;color:var(--ink)}

/* partners */
.partners{position:absolute;left:0;top:1336px;width:1200px;height:86px;background:var(--mint);display:flex;align-items:center}
.partner{position:absolute;top:30px;display:flex;align-items:center;gap:8px;font-size:24px;color:#3a3a3a}
.partner b{display:block;width:22px;height:22px;border-radius:50%;background:#6b6b6b}

/* testimonials */
.section-title{position:absolute;left:0;width:1200px;text-align:center;font-size:26px;font-weight:700;color:var(--ink)}
.quote{position:absolute;top:1523px;width:226px;height:360px;background:var(--green);color:var(--white);text-align:center;box-shadow:6px 8px 8px rgba(0,0,0,.35)}
.quote svg{display:block;margin:18px auto 0}
.quote h4{font-size:18px;font-weight:700;margin-top:14px}
.quote p{font-size:14.6px;line-height:18.5px;margin:20px 14px 0}

/* posts */
.post{position:absolute;top:1972px;width:260px;display:flex;gap:10px}
.date{width:46px;flex:none;text-align:center;border-radius:4px;overflow:hidden}
.date .m{background:#1a1a1a;color:var(--white);font-size:21px;height:38px;line-height:38px}
.date .d{background:var(--green);color:var(--white);font-size:19px;height:32px;line-height:32px}
.post p{font-size:14.5px;line-height:17px;color:#555;font-family:"Verdana","Arimo",sans-serif;letter-spacing:-0.3px}

/* footer */
.site-footer{position:absolute;left:0;top:2113px;width:1200px;height:316px;background:var(--footer);color:var(--white)}
.fcol{position:absolute;top:20px}
.fcol h5{font-size:15.5px;color:var(--green);font-weight:700;margin-bottom:30px}
.fcol li{list-style:none;font-size:15px;line-height:26px}
.fcol address{font-style:normal;font-size:15px;line-height:20px}
.socials{display:flex;gap:7px;margin-top:14px}
.socials i{display:block;width:26px;height:26px;border-radius:50%;border:1.5px solid var(--green)}
.signup{position:absolute;left:834px;top:83px;display:flex}
.signup span{width:128px;height:30px;background:#e9e9e9;color:#888;font-size:12.5px;line-height:30px;padding-left:10px}
.signup b{background:var(--green);font-size:13.5px;font-weight:400;height:30px;line-height:30px;padding:0 6px}
.copyright{position:absolute;left:360px;top:2365px;width:495px;border-top:1px solid #333;text-align:center;color:#bbb;font-size:10.5px;padding-top:28px}
</style>
</head>
<body>

<header class="site-header">
  <div class="brand">Velmo</div>
  <nav class="main-nav">
    <span>Home</span><span>About Us</span><span>Services</span><span>Advice<i class="caret"></i></span><span>Advisers Profile</span><span>Login</span><span>Sign Up</span><span>Help</span>
  </nav>
</header>

<section class="hero" role="img" aria-label="Sepia photograph of a hand with a pen over paperwork">
  <div class="hero-panel">
    <h1>Welcome to Velmo</h1>
    <p>Dummy text is text that is used in the publishing industry or by web designers to occupy the space which will later be filled with 'real' content. This is required when, for example, the final text is not yet available. Dummy text is also known as 'fill text'. It is said that song composers of the past used dummy texts as lyrics when writing melodies in order to have a 'ready-made' text to sing with the melody. Dummy texts have been in use by typesetters since the 16th century.</p>
    <span class="btn-outline">More</span>
  </div>
  <div class="hero-actions"><span>Register Your Business</span><span>Register as an Advisor</span></div>
  <div class="dots"><i></i><i></i><i></i></div>
</section>

<!-- services -->
<svg width="0" height="0" style="position:absolute">
  <defs>
    <g id="bubble">
      <path d="M14 3h111a11 11 0 0 1 11 11v60a11 11 0 0 1-11 11H104l-14 12-3-12H14A11 11 0 0 1 3 74V14A11 11 0 0 1 14 3z" fill="#fff" stroke="#1eb872" stroke-width="6" stroke-linejoin="round"/>
    </g>
  </defs>
</svg>

<div class="service" style="left:176px">
  <svg width="140" height="100" viewBox="0 0 140 100"><use href="#bubble"/>
    <rect x="44" y="26" width="40" height="26" fill="#1b1b1b" transform="rotate(-18 64 39)"/>
    <circle cx="64" cy="39" r="6" fill="#fff" transform="rotate(-18 64 39)"/>
    <rect x="58" y="48" width="28" height="18" rx="5" fill="#1b1b1b"/>
  </svg>
  <h2>Debt funding advice</h2>
  <p>Dummy text is also used to demonstrate the appearance of different typefaces and layouts, and in general the content of dummy text is nonsensical.</p>
  <span class="btn-more">More</span>
</div>
<div class="service" style="left:394px">
  <svg width="140" height="100" viewBox="0 0 140 100"><use href="#bubble"/>
    <g fill="#1b1b1b" stroke="#1b1b1b" stroke-width="3">
      <line x1="70" y1="18" x2="70" y2="66"/><line x1="44" y1="28" x2="96" y2="28"/>
      <path d="M44 28l-10 22h20z" fill="none" stroke-width="2"/><path d="M34 50a10 6 0 0 0 20 0z"/>
      <path d="M96 28l-10 22h20z" fill="none" stroke-width="2"/><path d="M86 50a10 6 0 0 0 20 0z"/>
      <rect x="56" y="66" width="28" height="5"/>
    </g>
  </svg>
  <h2>Legal advice</h2>
  <p>Dummy text is also used to demonstrate the appearance of different typefaces and layouts, and in general the content of dummy text is nonsensical.</p>
  <span class="btn-more">More</span>
</div>
<div class="service" style="left:610px">
  <svg width="140" height="100" viewBox="0 0 140 100"><use href="#bubble"/>
    <rect x="50" y="16" width="40" height="56" rx="4" fill="#1b1b1b"/>
    <rect x="56" y="22" width="28" height="12" fill="#fff"/>
    <g fill="#fff"><rect x="56" y="40" width="7" height="7"/><rect x="67" y="40" width="7" height="7"/><rect x="78" y="40" width="7" height="7"/><rect x="56" y="52" width="7" height="7"/><rect x="67" y="52" width="7" height="7"/><rect x="78" y="52" width="7" height="14"/><rect x="56" y="62" width="18" height="5"/></g>
  </svg>
  <h2>Accountant advice</h2>
  <p>Dummy text is also used to demonstrate the appearance of different typefaces and layouts, and in general the content of dummy text is nonsensical.</p>
  <span class="btn-more">More</span>
</div>
<div class="service" style="left:832px">
  <svg width="140" height="100" viewBox="0 0 140 100"><use href="#bubble"/>
    <rect x="58" y="16" width="22" height="10" rx="2" fill="none" stroke="#1b1b1b" stroke-width="4"/>
    <rect x="40" y="24" width="58" height="42" rx="4" fill="#1b1b1b"/>
    <line x1="40" y1="40" x2="98" y2="40" stroke="#fff" stroke-width="2"/>
    <circle cx="96" cy="62" r="13" fill="#1b1b1b" stroke="#fff" stroke-width="2"/>
    <text x="96" y="68" font-size="16" font-weight="700" fill="#fff" text-anchor="middle" font-family="Arimo,sans-serif">$</text>
  </svg>
  <h2>Analysis</h2>
  <p>Dummy text is also used to demonstrate the appearance of different typefaces and layouts, and in general the content of dummy text is nonsensical.</p>
  <span class="btn-more">More</span>
</div>

<div class="feature" style="left:176px">
  <h3>Who We Are</h3>
  <div class="ph" role="img" aria-label="Photo of a hand pointing at financial charts" style="background:linear-gradient(135deg,#b78f6e,#e8e3dc 60%,#8fa3c4)"></div>
  <p>Its function as a filler or as a tool for comparing the visual impression of different typefaces</p>
</div>
<div class="feature" style="left:474px">
  <h3>What We Do</h3>
  <div class="ph" role="img" aria-label="Photo of colleagues working together at a desk" style="background:linear-gradient(135deg,#d9d2c5,#7b6c5c 50%,#c8c2b8)"></div>
  <p>Its function as a filler or as a tool for comparing the visual impression of different typefaces</p>
</div>
<div class="feature" style="left:772px">
  <h3>Why choose Us</h3>
  <div class="ph" role="img" aria-label="Photo of a businessman touching a network diagram" style="background:linear-gradient(135deg,#2a6fb0,#8fc3ea 50%,#1d3f6a)"></div>
  <p>Its function as a filler or as a tool for comparing the visual impression of different typefaces</p>
</div>

<section class="partners" aria-label="Partners">
  <div class="partner" style="left:183px">Quantiva</div>
  <div class="partner" style="left:384px"><b></b>Orbisel</div>
  <div class="partner" style="left:530px">Kelvane</div>
  <div class="partner" style="left:744px"><b></b>Trendo</div>
  <div class="partner" style="left:916px"><b></b>Lumacell</div>
</section>

<h2 class="section-title" style="top:1455px">What our customers have to say</h2>

<svg width="0" height="0" style="position:absolute">
  <defs>
    <radialGradient id="portrait" cx="50%" cy="45%" r="55%"><stop offset="0" stop-color="#d8d8d8"/><stop offset="1" stop-color="#9a9a9a"/></radialGradient>
    <g id="avatar">
      <path d="M62 3a59 59 0 1 1-42 101l-16 12 6-22A59 59 0 0 1 62 3z" fill="#fff"/>
      <circle cx="62" cy="62" r="50" fill="url(#portrait)"/>
    </g>
  </defs>
</svg>

<article class="quote" style="left:176px">
  <svg width="124" height="120" viewBox="0 0 124 120" role="img" aria-label="Customer portrait"><use href="#avatar"/></svg>
  <h4>Ria Colton</h4>
  <p>Dummy text is also used to demonstrate the appearance of different typefaces and layouts, and in general the content of dummy text is nonsensical.</p>
</article>
<article class="quote" style="left:486px">
  <svg width="124" height="120" viewBox="0 0 124 120" role="img" aria-label="Customer portrait"><use href="#avatar"/></svg>
  <h4>Ria Colton</h4>
  <p>Dummy text is also used to demonstrate the appearance of different typefaces and layouts, and in general the content of dummy text is nonsensical.</p>
</article>
<article class="quote" style="left:800px">
  <svg width="124" height="120" viewBox="0 0 124 120" role="img" aria-label="Customer portrait"><use href="#avatar"/></svg>
  <h4>Ria Colton</h4>
  <p>Dummy text is also used to demonstrate the appearance of different typefaces and layouts, and in general the content of dummy text is nonsensical.</p>
</article>

<h2 class="section-title" style="top:1920px">Recent Posts</h2>

<div class="post" style="left:176px">
  <div class="date"><div class="m">Aug</div><div class="d">31</div></div>
  <p>Lorem Ipsum is simply dummy text of the printing and typesetting industry. Lorem Ipsum has been the industry's standard dummy text</p>
</div>
<div class="post" style="left:470px">
  <div class="date"><div class="m">Aug</div><div class="d">28</div></div>
  <p>Lorem Ipsum is simply dummy text of the printing and typesetting industry. Lorem Ipsum has been the industry's standard dummy text</p>
</div>
<div class="post" style="left:759px">
  <div class="date"><div class="m">Aug</div><div class="d">25</div></div>
  <p>Lorem Ipsum is simply dummy text of the printing and typesetting industry. Lorem Ipsum has been the industry's standard dummy text</p>
</div>

<footer class="site-footer">
  <div class="fcol" style="left:180px"><h5>ABOUT</h5><ul><li>Company Info</li><li>Services</li><li>Clints</li><li>Solutions</li></ul></div>
  <div class="fcol" style="left:392px"><h5>GET IN TOUCH</h5><ul><li>Login</li><li>Sign Up</li><li>Register</li><li>Blog</li></ul></div>
  <div class="fcol" style="left:618px"><h5>GET IN TOUCH</h5>
    <address>Velmo services,<br>42-48 Harbour Lane,<br>AU.</address>
    <address style="margin-top:10px;line-height:24px">info@velmo.co.uk<br>support@velmo.co.uk</address>
    <div class="socials"><i></i><i></i><i></i><i></i></div>
  </div>
  <div class="fcol" style="left:830px"><h5>STAY INFORMED</h5></div>
  <div class="signup"><span>Email address</span><b>SIGN UP</b></div>
</footer>
<div class="copyright">Copyright © 2007-2014 Velmoservices. All rights reserved.</div>

</body>
</html>
```